A reimagined website for a cross-border tax firm

There are two aspects to this project for Brackwell Tax Consultancy:
1) I need a logo update to accommodate increasing focus and specialization in my business. The byline under the name “Brackwell Tax Consultancy” needs to change:
ORIGINAL: FILING AID FOR CIVIC LEDGER PRACTICES
REVISED: CROSS-BORDER TAX SERVICES • U.S. & CANADA
2) I need a website “refresh” (see current website at www.levyhelpdesk.example) based on this logo – a new vision for a website with greater clarity, focus and organization. It should represent a re-envisioning of the current approach, and not the wholesale abandonment of the style represented there. I need it to be creative, compelling and attention grabbing, but still professional. This should, at a minimum, update any places where the old name/logo is used, but I want the redesign to go beyond this to something more intuitive. I need high quality separate PNG files of the various logo styles for use in various documents, but HTML coding would be a helpful but not necessary addition.

Target Market(s)

People in need of cross-border tax services - Canada and US

Coding

Number of Pages Required

Requirements
Must have
• Greater crispness, sharpness - higher resolution
• A more compelling, organized approach - make the wording and images more accessible to the website user (especially the staff bios, which have scroll bars now)
Nice to have
• Replacement of stock image with a true image of the Halifax skyline
Should not have
• Deviate from colour pattern represented in website logo of blue/orange
• Deviate from existing logo except for word replacement

```html
<!DOCTYPE html>
<html lang="en">
<head>
<meta charset="utf-8">
<title>Brackwell Tax Consultancy – Website Screens</title>
<link href="https://fonts.googleapis.com/css2?family=Tinos&family=Ubuntu:wght@400;500;700&display=swap" rel="stylesheet">
<style>
:root{
  --page:#ffffff;
  --rail:#d1d1d1;
  --rail-ink:#3a3a3a;
  --dark:#161616;
  --dark-2:#2b2b2b;
  --ink-light:#e9e9e9;
  --ink-mute:#9a9a9a;
  --line:#8a8a8a;
  --accent:#e08a1e;
  --field:#ffffff;
  --field-ink:#a5a5a5;
  --pin:#d8342c;
}
*{box-sizing:border-box;margin:0;padding:0}
html,body{width:1200px;height:1200px;overflow:hidden;background:var(--page)}
body{position:relative;font-family:"Ubuntu",sans-serif;color:var(--ink-light)}
.screen{position:absolute;width:470px;height:269px;overflow:hidden;
  background:radial-gradient(ellipse at 55% 35%,#3a3a3a 0%,#222 45%,#0e0e0e 100%)}
.screen .backdrop{position:absolute;left:51px;top:0;right:0;bottom:0;
  background:linear-gradient(100deg,rgba(0,0,0,.55) 0%,rgba(0,0,0,0) 30%,rgba(0,0,0,0) 70%,rgba(0,0,0,.55) 100%),
  linear-gradient(180deg,rgba(0,0,0,.2),rgba(0,0,0,.45))}
.s-home{left:124px;top:41px}
.s-testimonials{left:608px;top:41px}
.s-services{left:124px;top:322px}
.s-contact{left:608px;top:322px}
.s-team{left:124px;top:606px}
.s-payment{left:608px;top:606px}
.s-upload{left:608px;top:887px}

/* side navigation */
.nav{position:absolute;left:0;top:0;width:51px;height:100%;background:var(--rail);
  display:flex;flex-direction:column;align-items:center;padding-top:20px;z-index:2}
.nav-item{position:relative;width:51px;height:34.6px;display:flex;flex-direction:column;align-items:center;
  font-size:5px;color:var(--rail-ink)}
.nav-item svg{width:11px;height:11px;margin-bottom:2px;fill:none;stroke:#555;stroke-width:1.3;stroke-linecap:round;stroke-linejoin:round}
.nav-item.active::after{content:"";position:absolute;right:0;top:8px;border-style:solid;
  border-width:5px 5px 5px 0;border-color:transparent var(--dark) transparent transparent}

.content{position:absolute;left:51px;top:0;right:0;bottom:0;z-index:1}
.title{position:absolute;left:0;right:0;top:42px;text-align:center;font-family:"Tinos",serif;
  font-size:18px;letter-spacing:.3px;color:var(--ink-light)}
.copyright{position:absolute;left:0;right:0;top:256px;text-align:center;font-size:3.6px;color:#8c8c8c}
.lede{position:absolute;left:40px;right:40px;text-align:center;font-size:5.2px;line-height:8.4px;color:#dcdcdc}
.arrow{position:absolute;width:8px;height:8px;fill:none;stroke:#bbb;stroke-width:1.4}

/* home */
.brand{position:absolute;left:110px;top:108px;display:flex;align-items:center;gap:5px}
.brand-mark{width:14px;height:14px;background:var(--accent)}
.brand-name{font-family:"Tinos",serif;font-size:11.5px;color:#fff;text-transform:uppercase;letter-spacing:.3px}
.brand-byline{position:absolute;left:129px;top:124px;font-family:"Tinos",serif;font-size:5.2px;letter-spacing:1.3px;color:#ddd}

/* testimonials */
.quote-mark{position:absolute;font-family:"Tinos",serif;font-size:110px;line-height:1;color:rgba(255,255,255,.08)}
.card{position:absolute;top:115px;width:83px;height:86px;border:1px solid #8a8a8a;border-radius:2px;
  text-align:center;padding:12px 8px 0;color:#eee;background:rgba(0,0,0,.15)}
.card.featured{background:#fff;color:#222;border-color:#fff;top:114px;height:88px}
.card h4{font-size:6.2px;font-weight:700}
.card hr{width:18px;margin:6px auto 8px;border:0;border-top:1px solid currentColor;opacity:.7}
.card p{font-size:4px;line-height:7px}

/* services */
.choice{position:absolute;left:56px;width:307px;height:25px;padding-left:14px;display:flex;align-items:center;
  font-size:8px;font-weight:500}
.choice.primary{top:107px;background:#ececec;color:#222;border:2px solid #bdbdbd}
.choice.secondary{top:162px;color:#cfcfcf;border:1px solid #6a6a6a;background:rgba(0,0,0,.3)}
.popover{position:absolute;left:229px;top:135px;width:166px;height:119px;background:#fff;border-radius:3px;
  box-shadow:0 2px 8px rgba(0,0,0,.5);color:#333;padding:8px 0 0 9px}
.popover p{width:74px;font-size:3.9px;line-height:6.9px;margin-bottom:6px}
.popover .visual{position:absolute;left:88px;top:8px;width:70px;height:100px;
  background:linear-gradient(135deg,#dfe6ee 0%,#a9b8c8 50%,#6b7d91 100%)}

/* contact */
.map{position:absolute;left:42px;top:72px;width:336px;height:80px;
  background:linear-gradient(100deg,#dfe4d8 0%,#e9ebe3 40%,#d7dfcf 75%,#cdd9e2 100%)}
.pin{position:absolute;width:8px;height:11px}
.address{position:absolute;width:90px;height:24px;background:rgba(45,45,45,.88);color:#eee;font-size:3.6px;
  line-height:5px;padding:3px 5px}
.panel{position:absolute;border:1px solid #7d7d7d;background:rgba(10,10,10,.55)}
.message-panel{left:42px;top:152px;width:336px;height:94px}
.panel-title{position:absolute;left:0;right:0;top:10px;text-align:center;font-size:8.6px;color:#eee}
.field{position:absolute;height:12px;background:var(--field);font-size:4px;color:var(--field-ink);padding:3px 4px;border:1px solid #ccc}
.btn-light{position:absolute;height:11px;background:#f3f3f3;color:#222;font-size:5.5px;font-weight:700;
  display:flex;align-items:center;justify-content:center;border:1px solid #aaa}

/* team */
.portrait{position:absolute;width:60px;height:60px;background:linear-gradient(160deg,#d8d8d8 0%,#8d8d8d 55%,#3e3e3e 100%)}
.portrait.selected{outline:1.5px solid #eee}
.name-tag{position:absolute;left:293px;top:222px;width:58px;height:15px;background:#d9d9d9;color:#222;
  font-size:3.8px;padding:2px 5px;line-height:5px}
.name-tag b{font-style:italic;font-weight:700}

/* payment */
.pay-panel{left:99px;top:94px;width:221px;height:128px}
.pay-label{position:absolute;left:28px;top:15px;font-size:5.2px;color:#ddd}

/* upload */
.upload-sheet{position:absolute;left:42px;top:75px;width:336px;height:162px;background:#fff;color:#555}
.upload-sheet .band{height:12px;background:#ececec}
.hint{position:absolute;left:14px;top:21px;font-size:4px;color:#888}
.dropzone{position:absolute;left:14px;top:30px;width:308px;height:74px;border:1px dashed #b0b0b0;text-align:center}
.dropzone svg{width:22px;height:22px;margin-top:18px;fill:none;stroke:#888;stroke-width:1}
.dropzone .add{font-size:8px;color:#777;margin-top:1px}
.dropzone .sub{font-size:3.6px;color:#aaa;letter-spacing:.3px}
.file-bar{position:absolute;left:14px;top:109px;width:254px;height:14px;background:#ececec;font-size:3.8px;color:#999;padding:5px 6px}
.btn-dark{position:absolute;height:14px;background:#1e1e1e;color:#fff;font-size:3.8px;display:flex;align-items:center;justify-content:center;letter-spacing:.3px}
.btn-outline{position:absolute;height:14px;border:1px solid #777;color:#444;font-size:3.8px;display:flex;align-items:center;justify-content:center;letter-spacing:.3px}
</style>
</head>
<body>

<svg width="0" height="0" style="position:absolute" aria-hidden="true">
  <symbol id="i-home" viewBox="0 0 20 20"><path d="M2 10 L10 3 L18 10 M4.5 8.5 V17 H15.5 V8.5 M8 17 V12 H12 V17"/></symbol>
  <symbol id="i-services" viewBox="0 0 20 20"><path d="M3 3 L17 17 M17 3 L3 17"/><circle cx="4" cy="16" r="1.8"/><circle cx="16" cy="16" r="1.8"/></symbol>
  <symbol id="i-team" viewBox="0 0 20 20"><circle cx="7" cy="7" r="3"/><circle cx="13.5" cy="8" r="2.5"/><path d="M2 17 C2 12 12 12 12 17 M10 13 C12 11 18 11 18 16"/></symbol>
  <symbol id="i-chat" viewBox="0 0 20 20"><path d="M2 5 H12 V11 H6 L3 14 V11 H2 Z M8 13 V15 H13 L16 18 V15 H18 V8 H14"/></symbol>
  <symbol id="i-contact" viewBox="0 0 20 20"><circle cx="10" cy="9" r="6.5"/><circle cx="10" cy="9" r="2.5"/><path d="M6 17 H14"/></symbol>
  <symbol id="i-payment" viewBox="0 0 20 20"><path d="M3 11 L11 3 H17 V9 L9 17 Z"/><circle cx="13.5" cy="6.5" r="1.2"/><path d="M5 9 L11 15"/></symbol>
  <symbol id="i-upload" viewBox="0 0 20 20"><path d="M6 15 H4.5 A3.5 3.5 0 0 1 5 8 A5 5 0 0 1 14.5 7 A4 4 0 0 1 15.5 15 H14 M10 18 V10 M7 13 L10 10 L13 13"/></symbol>
  <symbol id="i-prev" viewBox="0 0 10 10"><path d="M7 1 L3 5 L7 9"/></symbol>
  <symbol id="i-next" viewBox="0 0 10 10"><path d="M3 1 L7 5 L3 9"/></symbol>
  <symbol id="i-pin" viewBox="0 0 8 11"><path d="M4 11 C1 7 0 5.5 0 4 A4 4 0 0 1 8 4 C8 5.5 7 7 4 11 Z" fill="var(--pin)" stroke="none"/><circle cx="4" cy="4" r="1.4" fill="#7a1410" stroke="none"/></symbol>
</svg>

<!-- Home -->
<section class="screen s-home">
  <div class="backdrop" role="img" aria-label="Dark upward view of city towers"></div>
  <nav class="nav">
    <div class="nav-item active"><svg><use href="#i-home"/></svg>Home</div>
    <div class="nav-item"><svg><use href="#i-services"/></svg>Services</div>
    <div class="nav-item"><svg><use href="#i-team"/></svg>Team</div>
    <div class="nav-item"><svg><use href="#i-chat"/></svg>Testimonials</div>
    <div class="nav-item"><svg><use href="#i-contact"/></svg>Contact</div>
    <div class="nav-item"><svg><use href="#i-payment"/></svg>Payment</div>
    <div class="nav-item"><svg><use href="#i-upload"/></svg>File upload</div>
  </nav>
  <div class="content">
    <div class="brand"><span class="brand-mark"></span><span class="brand-name">Brackwell Tax Consultancy</span></div>
    <div class="brand-byline">CROSS-BORDER TAX SERVICES • U.S. &amp; CANADA</div>
    <p class="lede" style="top:146px">Lorem ipsum dolor sit amet, consectetur adipiscing elit, sed do eiusmod tempor incididunt ut labore et dolore magna aliqua. Lorem ipsum dolor sit amet, consectetur adipiscing elit, sed do eiusmod tempor incididunt ut labore et dolore magna aliqua.</p>
    <p class="copyright">Copyright © 2017 Brackwell Tax Consultancy Inc.</p>
  </div>
</section>

<!-- Testimonials -->
<section class="screen s-testimonials">
  <div class="backdrop" role="img" aria-label="Dark upward view of city towers"></div>
  <nav class="nav">
    <div class="nav-item"><svg><use href="#i-home"/></svg>Home</div>
    <div class="nav-item"><svg><use href="#i-services"/></svg>Services</div>
    <div class="nav-item"><svg><use href="#i-team"/></svg>Team</div>
    <div class="nav-item active"><svg><use href="#i-chat"/></svg>Testimonials</div>
    <div class="nav-item"><svg><use href="#i-contact"/></svg>Contact</div>
    <div class="nav-item"><svg><use href="#i-payment"/></svg>Payment</div>
    <div class="nav-item"><svg><use href="#i-upload"/></svg>File upload</div>
  </nav>
  <div class="content">
    <span class="quote-mark" style="left:38px;top:10px">“</span>
    <span class="quote-mark" style="left:325px;top:200px">”</span>
    <h2 class="title">TESTIMONIALS</h2>
    <svg class="arrow" style="left:54px;top:153px"><use href="#i-prev"/></svg>
    <div class="card" style="left:80px"><h4>Owen Carrick</h4><hr><p>Lorem ipsum dolor sit amet, consectetur adipiscing elit, sed do eiusmod tempor incididunt ut labore et dolore magna aliqua. Lorem ipsum dolor sit amet.</p></div>
    <div class="card featured" style="left:169px"><h4>Owen Carrick</h4><hr><p>Lorem ipsum dolor sit amet, consectetur adipiscing elit, sed do eiusmod tempor incididunt ut labore et dolore magna aliqua. Lorem ipsum dolor sit amet.</p></div>
    <div class="card" style="left:257px"><h4>Owen Carrick</h4><hr><p>Lorem ipsum dolor sit amet, consectetur adipiscing elit, sed do eiusmod tempor incididunt ut labore et dolore magna aliqua. Lorem ipsum dolor sit amet.</p></div>
    <svg class="arrow" style="left:362px;top:153px"><use href="#i-next"/></svg>
    <p class="copyright">Copyright © 2017 Brackwell Tax Consultancy Inc.</p>
  </div>
</section>

<!-- Services -->
<section class="screen s-services">
  <div class="backdrop" role="img" aria-label="Dark upward view of city towers"></div>
  <nav class="nav">
    <div class="nav-item"><svg><use href="#i-home"/></svg>Home</div>
    <div class="nav-item active"><svg><use href="#i-services"/></svg>Services</div>
    <div class="nav-item"><svg><use href="#i-team"/></svg>Team</div>
    <div class="nav-item"><svg><use href="#i-chat"/></svg>Testimonials</div>
    <div class="nav-item"><svg><use href="#i-contact"/></svg>Contact</div>
    <div class="nav-item"><svg><use href="#i-payment"/></svg>Payment</div>
    <div class="nav-item"><svg><use href="#i-upload"/></svg>File upload</div>
  </nav>
  <div class="content">
    <h2 class="title">OUR SERVICES</h2>
    <div class="choice primary">I am an individual or business in need of tax services for myself</div>
    <div class="choice secondary">I am a public accountant in need of tax support</div>
    <div class="popover">
      <p>Lorem ipsum dolor sit amet, consectetur adipiscing elit, sed do eiusmod tempor incididunt ut labore et dolore magna aliqua. Lorem ipsum dolor sit amet, consectetur adipiscing elit, sed do eiusmod tempor incididunt ut labore et dolore magna aliqua.</p>
      <p>Sed do eiusmod tempor incididunt ut labore et dolore magna aliqua. Lorem ipsum dolor sit amet, consectetur adipiscing elit, sed do eiusmod tempor incididunt ut labore et dolore magna aliqua.</p>
      <div class="visual" role="img" aria-label="Photo of two people reviewing charts on a tablet"></div>
    </div>
    <p class="copyright">Copyright © 2017 Brackwell Tax Consultancy Inc.</p>
  </div>
</section>

<!-- Contact -->
<section class="screen s-contact">
  <div class="backdrop" role="img" aria-label="Dark upward view of city towers"></div>
  <nav class="nav">
    <div class="nav-item"><svg><use href="#i-home"/></svg>Home</div>
    <div class="nav-item"><svg><use href="#i-services"/></svg>Services</div>
    <div class="nav-item"><svg><use href="#i-team"/></svg>Team</div>
    <div class="nav-item"><svg><use href="#i-chat"/></svg>Testimonials</div>
    <div class="nav-item active"><svg><use href="#i-contact"/></svg>Contact</div>
    <div class="nav-item"><svg><use href="#i-payment"/></svg>Payment</div>
    <div class="nav-item"><svg><use href="#i-upload"/></svg>File upload</div>
  </nav>
  <div class="content">
    <h2 class="title">CONTACT US</h2>
    <div class="map" role="img" aria-label="Street map showing the two office locations"></div>
    <svg class="pin" style="left:111px;top:96px"><use href="#i-pin"/></svg>
    <svg class="pin" style="left:303px;top:91px"><use href="#i-pin"/></svg>
    <div class="address" style="left:89px;top:112px">118 Harbourline Road, Unit 6<br>Eastport, Nova Scotia, Canada B0X 2Z4<br>Phone: (555) 014-2207<br>Fax: (555) 014-2290</div>
    <div class="address" style="left:230px;top:112px">118 Harbourline Road, Unit 6<br>Eastport, Nova Scotia, Canada B0X 2Z4<br>Phone: (555) 014-2207<br>Fax: (555) 014-2290</div>
    <div class="panel message-panel">
      <div class="panel-title">Send Us A Message</div>
    </div>
    <div class="field" style="left:78px;top:181px;width:64px">Name</div>
    <div class="field" style="left:146px;top:181px;width:62px">Phone</div>
    <div class="field" style="left:212px;top:181px;width:130px">E-mail Address</div>
    <div class="field" style="left:78px;top:196px;width:264px;height:27px">Message</div>
    <div class="btn-light" style="left:179px;top:227px;width:63px">Send</div>
    <p class="copyright">Copyright © 2017 Brackwell Tax Consultancy Inc.</p>
  </div>
</section>

<!-- Team -->
<section class="screen s-team">
  <div class="backdrop" role="img" aria-label="Dark upward view of city towers"></div>
  <nav class="nav">
    <div class="nav-item"><svg><use href="#i-home"/></svg>Home</div>
    <div class="nav-item"><svg><use href="#i-services"/></svg>Services</div>
    <div class="nav-item active"><svg><use href="#i-team"/></svg>Team</div>
    <div class="nav-item"><svg><use href="#i-chat"/></svg>Testimonials</div>
    <div class="nav-item"><svg><use href="#i-contact"/></svg>Contact</div>
    <div class="nav-item"><svg><use href="#i-payment"/></svg>Payment</div>
    <div class="nav-item"><svg><use href="#i-upload"/></svg>File upload</div>
  </nav>
  <div class="content">
    <h2 class="title">OUR TEAM</h2>
    <p class="lede" style="top:74px">Lorem ipsum dolor sit amet, consectetur adipiscing elit, sed do eiusmod tempor incididunt ut labore et dolore magna aliqua. Lorem ipsum dolor sit amet, consectetur adipiscing elit, sed do eiusmod tempor incididunt ut labore et dolore magna aliqua.</p>
    <svg class="arrow" style="left:54px;top:174px"><use href="#i-prev"/></svg>
    <div class="portrait" style="left:111px;top:113px" role="img" aria-label="Black and white staff portrait"></div>
    <div class="portrait" style="left:180px;top:113px" role="img" aria-label="Black and white staff portrait"></div>
    <div class="portrait" style="left:249px;top:113px" role="img" aria-label="Black and white staff portrait"></div>
    <div class="portrait" style="left:111px;top:182px" role="img" aria-label="Black and white staff portrait"></div>
    <div class="portrait" style="left:180px;top:182px" role="img" aria-label="Black and white staff portrait"></div>
    <div class="portrait selected" style="left:249px;top:182px" role="img" aria-label="Black and white staff portrait, selected"></div>
    <div class="name-tag"><b>Daniel R. Foss, CGA</b><br>Know More</div>
    <svg class="arrow" style="left:362px;top:174px"><use href="#i-next"/></svg>
    <p class="copyright">Copyright © 2017 Brackwell Tax Consultancy Inc.</p>
  </div>
</section>

<!-- Payment -->
<section class="screen s-payment">
  <div class="backdrop" role="img" aria-label="Dark upward view of city towers"></div>
  <nav class="nav">
    <div class="nav-item"><svg><use href="#i-home"/></svg>Home</div>
    <div class="nav-item"><svg><use href="#i-services"/></svg>Services</div>
    <div class="nav-item"><svg><use href="#i-team"/></svg>Team</div>
    <div class="nav-item"><svg><use href="#i-chat"/></svg>Testimonials</div>
    <div class="nav-item"><svg><use href="#i-contact"/></svg>Contact</div>
    <div class="nav-item active"><svg><use href="#i-payment"/></svg>Payment</div>
    <div class="nav-item"><svg><use href="#i-upload"/></svg>File upload</div>
  </nav>
  <div class="content">
    <h2 class="title">PAYMENT OPTION</h2>
    <div class="panel pay-panel"><div class="pay-label">Credit / Debit / ATM Card</div></div>
    <div class="field" style="left:128px;top:129px;width:80px">Name</div>
    <div class="field" style="left:210px;top:129px;width:82px">E-mail Address</div>
    <div class="field" style="left:128px;top:148px;width:164px">Card Number</div>
    <div class="field" style="left:128px;top:166px;width:80px">Invoice Number</div>
    <div class="field" style="left:210px;top:166px;width:82px">Amount</div>
    <div class="field" style="left:128px;top:185px;width:52px">Expiry <span style="color:#333">MM ▾ &nbsp;YY ▾</span></div>
    <div class="field" style="left:182px;top:185px;width:46px">CVV</div>
    <div class="btn-light" style="left:232px;top:185px;width:60px;height:12px">Submit</div>
    <p class="copyright">Copyright © 2017 Brackwell Tax Consultancy Inc.</p>
  </div>
</section>

<!-- File upload -->
<section class="screen s-upload">
  <div class="backdrop" role="img" aria-label="Dark upward view of city towers"></div>
  <nav class="nav">
    <div class="nav-item"><svg><use href="#i-home"/></svg>Home</div>
    <div class="nav-item"><svg><use href="#i-services"/></svg>Services</div>
    <div class="nav-item"><svg><use href="#i-team"/></svg>Team</div>
    <div class="nav-item"><svg><use href="#i-chat"/></svg>Testimonials</div>
    <div class="nav-item"><svg><use href="#i-contact"/></svg>Contact</div>
    <div class="nav-item"><svg><use href="#i-payment"/></svg>Payment</div>
    <div class="nav-item active"><svg><use href="#i-upload"/></svg>File upload</div>
  </nav>
  <div class="content">
    <h2 class="title">FILE UPLOAD</h2>
    <div class="upload-sheet">
      <div class="band"></div>
      <p class="hint">Please fill out your form with available fields</p>
      <div class="dropzone">
        <svg viewBox="0 0 22 22"><path d="M2 6 V20 H16"/><rect x="6" y="2" width="14" height="14"/><path d="M13 5 V13 M9 9 H17"/></svg>
        <div class="add">ADD FILES</div>
        <div class="sub">SIMPLY DRAG AND DROP</div>
      </div>
      <div class="file-bar">File Name / location</div>
      <div class="btn-dark" style="left:270px;top:109px;width:52px">ADD FILES</div>
      <div class="btn-outline" style="left:115px;top:130px;width:52px">PREVIEW</div>
      <div class="btn-dark" style="left:170px;top:130px;width:52px">SUBMIT</div>
    </div>
    <p class="copyright">Copyright © 2017 Brackwell Tax Consultancy Inc.</p>
  </div>
</section>

</body>
</html>
```